rose gold typography style landscape business card | upmarket tanning lounge

After years of receiving spray tans, we are two young professionals starting our own spray tanning business. Our point of difference is offering a complete tanning experience within a fun, edgy yet professional atmosphere.
Our ideal card would draw upon design elements from the typography example we have attached. We are hoping to have "velmira" in all lowercase in the typography style, with "TANNING LOUNGE" in much smaller uppercase font underneath but closely positioned below "velmira".
We have attached an example of a business card created by a designer on here - we like how the word on the front almost goes beyond the edges of the card itself.
But you have the design know how, so please let your creative juices flow!
We are thinking either rose gold text (matte rather than a chrome look) with a white background or rose gold freehand style typography with a charcoal background using landscape orientation. We have opted for a thicker style edgy typography to accommodate the metallic look font we are looking for.
We cannot wait to see what you create! Thanks in advance.
Harriet & Jocelyn
Project Deadline Extended
Reason: Firstly, we wish to thank each and every one of you who have provided a submission for our project. You guys are amazingly talented and we've loved watching all the designs come through.
We have decided to take our top four favourite designs to a poll with our friends and family and will therefore need to extend the deadline by a couple of days.
We do apologise for any inconvenience this may have caused and thank you for your patience and understanding!
Harriet & Jocelyn

```html
<!DOCTYPE html>
<html lang="en">
<head>
<meta charset="utf-8">
<title>velmira tanning lounge – business card</title>
<link rel="stylesheet" href="https://fonts.googleapis.com/css2?family=Jost:wght@400&display=swap">
<style>
  :root {
    --charcoal: #20272a;
    --rose-gold: #cf9c78;
    --champagne: #ecd09a;
  }
  html, body {
    margin: 0;
    padding: 0;
    width: 1200px;
    height: 686px;
    overflow: hidden;
    background: var(--charcoal);
  }
  .card {
    position: relative;
    width: 1200px;
    height: 686px;
    background: var(--charcoal);
    overflow: hidden;
    font-family: "Jost", "Century Gothic", sans-serif;
    font-weight: 400;
  }
  .wordmark {
    position: absolute;
    left: 108px;
    top: 0;
    margin: 0;
    font-size: 320px;
    font-weight: 400;
    line-height: 1;
    letter-spacing: -2px;
    color: var(--rose-gold);
    white-space: nowrap;
  }
  .tagline {
    position: absolute;
    left: 309px;
    top: 283px;
    margin: 0;
    font-size: 41px;
    line-height: 1;
    letter-spacing: 0.5px;
    color: var(--champagne);
  }
  .contact-name {
    position: absolute;
    left: 115px;
    top: 570px;
    margin: 0;
    font-size: 27px;
    line-height: 1;
    letter-spacing: 0.5px;
    color: var(--champagne);
  }
  .contact-lines {
    position: absolute;
    left: 115px;
    top: 615px;
    display: flex;
    align-items: center;
    gap: 42px;
    font-size: 27px;
    line-height: 1;
    color: var(--champagne);
  }
  .contact-item {
    display: flex;
    align-items: center;
    gap: 4px;
  }
  .contact-item svg { display: block; }
</style>
</head>
<body>
  <main class="card">
    <h1 class="wordmark">velmira</h1>
    <p class="tagline">TANNING LOUNGE</p>

    <p class="contact-name">HARRIET LASTNAME</p>
    <div class="contact-lines">
      <span class="contact-item">
        <svg class="icon-phone" width="20" height="20" viewBox="0 0 20 20" aria-hidden="true">
          <rect x="0" y="0" width="20" height="20" rx="3" fill="var(--champagne)"/>
          <path d="M6.2 4.2c.6-.4 1.3-.2 1.6.4l1 1.8c.3.5.1 1.1-.3 1.4l-.8.6c.6 1.4 1.6 2.6 2.9 3.4l.6-.8c.4-.4 1-.5 1.4-.2l1.8 1.1c.5.3.7 1 .3 1.5l-.8 1.1c-.5.6-1.3.8-2 .5-3.2-1.4-5.6-4.1-6.6-7.5-.2-.7.1-1.5.7-1.9z" fill="var(--charcoal)"/>
        </svg>
        555.014.2387
      </span>
      <span class="contact-item">
        <svg class="icon-mail" width="18" height="14" viewBox="0 0 18 14" aria-hidden="true">
          <rect x="0" y="1" width="18" height="12" fill="var(--champagne)"/>
          <path d="M0 1.5 L9 8 L18 1.5" fill="none" stroke="var(--charcoal)" stroke-width="1.4"/>
        </svg>
        harriet@email.com
      </span>
    </div>
  </main>
</body>
</html>
```